brolvin business card design so that it looks better

need a new business card designed. use our website, brolvix.example for example. I attached an example of a previous card we had and liked. this is for law enforcement and we have attached a previous business card as an example. This site forces me to select color and font, ignore those as I picked stuff just to get this completed.

Target Market(s)

law enforcement, local government

Contact Information for Business Card

see the attached example and our website

Font styles to use
Serif

```html
<!DOCTYPE html>
<html lang="en">
<head>
<meta charset="utf-8">
<title>Brolvin Business Card</title>
<link href="https://fonts.googleapis.com/css2?family=Exo+2:wght@300;500&family=Roboto:wght@300;400&display=swap" rel="stylesheet">
<style>
  :root {
    --backdrop: #d4d4d4;
    --navy: #04121d;
    --navy-soft: #0c2230;
    --brand-blue: #0a6aa8;
    --silver-light: #f2f3f4;
    --silver-mid: #d9dcdf;
    --silver-deep: #c3c7cc;
    --ink: #1b1f24;
    --ink-soft: #2b3035;
    --white: #ffffff;
  }
  * { margin: 0; padding: 0; box-sizing: border-box; }
  html, body { width: 1200px; height: 576px; overflow: hidden; }
  body { background: var(--backdrop); position: relative; font-family: "Roboto", Arial, sans-serif; }

  .card {
    position: absolute; top: 138px; width: 484px; height: 294px;
    border-radius: 14px; overflow: hidden;
    box-shadow: 0 2px 6px rgba(0,0,0,0.18);
  }
  .card-front { left: 82px; background: var(--navy); }
  .card-back {
    left: 602px;
    background: linear-gradient(100deg, var(--silver-light) 0%, var(--silver-mid) 55%, var(--silver-deep) 100%);
  }

  .network-map {
    position: absolute; left: 30px; top: 30px; width: 420px; height: 240px;
    background: radial-gradient(ellipse at 50% 50%, var(--navy-soft) 0%, rgba(12,34,48,0) 70%);
  }

  .wordmark {
    font-family: "Exo 2", Arial, sans-serif; font-weight: 300;
    letter-spacing: 3px; line-height: 1; white-space: nowrap;
  }
  .card-front .wordmark {
    position: absolute; left: 0; right: 0; top: 128px; text-align: center;
    font-size: 58px; color: var(--white);
  }
  .card-back .wordmark {
    position: absolute; left: 29px; top: 36px; font-size: 48px; color: var(--ink);
  }

  .footer-bands { position: absolute; left: 0; bottom: 0; width: 484px; height: 24px; }
  .footer-url {
    position: absolute; right: 20px; bottom: 9px;
    font-size: 11px; letter-spacing: 2.2px; font-weight: 300;
    white-space: nowrap; line-height: 1;
  }
  .card-front .footer-url { color: var(--white); }
  .card-back .footer-url { color: var(--ink); }

  .person-name {
    position: absolute; left: 26px; top: 108px;
    font-family: "Exo 2", Arial, sans-serif; font-weight: 500;
    font-size: 20px; color: var(--brand-blue);
  }
  .person-title {
    position: absolute; left: 26px; top: 135px; font-size: 11.5px; color: var(--ink-soft);
  }
  .contact-list { position: absolute; left: 26px; top: 166px; list-style: none; }
  .contact-list li {
    display: flex; align-items: center; gap: 12px;
    font-size: 12.5px; color: var(--ink-soft); height: 18.5px;
  }
  .contact-list svg { width: 11px; height: 11px; fill: var(--brand-blue); }
  .address { position: absolute; left: 26px; top: 228px; font-size: 12.5px; color: var(--ink); }
</style>
</head>
<body>

  <section class="card card-front">
    <div class="network-map" role="img" aria-label="Faint network map of the United States"></div>
    <div class="wordmark">BROLVIN</div>
    <svg class="footer-bands" viewBox="0 0 484 24" aria-hidden="true">
      <polygon points="0,2 192,2 180,24 0,24" fill="var(--brand-blue)"/>
      <polygon points="212,2 270,2 258,24 200,24" fill="var(--white)"/>
    </svg>
    <div class="footer-url">www.brolvix.example</div>
  </section>

  <section class="card card-back">
    <div class="wordmark">BROLVIN</div>
    <div class="person-name">Dana Merrow</div>
    <div class="person-title">Founder/Chief Executive Officer</div>
    <ul class="contact-list">
      <li>
        <svg viewBox="0 0 12 12" aria-hidden="true"><path d="M1 4 C1 2 3 1.5 6 1.5 C9 1.5 11 2 11 4 L8.5 4.5 L8 3.5 L4 3.5 L3.5 4.5 Z M3 5 L9 5 L10.5 10.5 L1.5 10.5 Z"/></svg>
        555.014.2290
      </li>
      <li>
        <svg viewBox="0 0 12 12" aria-hidden="true"><path d="M1 2.5 H11 V9.5 H1 Z M1.8 3.2 L6 6.5 L10.2 3.2" fill="var(--brand-blue)" stroke="var(--silver-light)" stroke-width="0.8"/></svg>
        info@brolvix.example
      </li>
      <li>
        <svg viewBox="0 0 12 12" aria-hidden="true"><circle cx="6" cy="6" r="5"/><path d="M1 6 H11 M6 1 C4 3 4 9 6 11 M6 1 C8 3 8 9 6 11" stroke="var(--silver-light)" stroke-width="0.8" fill="none"/></svg>
        www.brolvix.example
      </li>
    </ul>
    <div class="address">4120 Larkfield Road Corvale, TX 70000</div>
    <svg class="footer-bands" viewBox="0 0 484 24" aria-hidden="true">
      <polygon points="0,3 218,3 206,24 0,24" fill="var(--brand-blue)"/>
      <polygon points="232,3 288,3 276,24 220,24" fill="var(--navy)"/>
    </svg>
    <div class="footer-url">www.brolvix.example</div>
  </section>

</body>
</html>
```